Business Card Design Project

I need a new business card for side business. Very simple and to the point. I am a licensed massage therapist and want the colors to be warm. I don't have a logo or company name. I just need to convey that I am a Licensed Massage Therapist and have my contact information so people can contact me. I'll attach some files that I like. I am a male so I don't want it to be feminine.

One file is my existing card. I like Tamsin's card and the layout so would prefer a similar layout. I would like to incorporate my swimmer/biker/runner image. Doesn't have to be the exact likeness because I don't have that file but something similar to that. I would like to also include my areas of specialty of: Swedish, Deep Tissue, Sports, and Hot Stone

I would also like to incorporate a QR code on the back of the card centered.
Updates

Payment is NOW guaranteed to the design I choose.  I updated my creative brief so hopefully it is more clear.  

Industry/Entity Type

Massage

Requirements
Must have
• Gavin Thrushwell
Licensed Massage Therapist
or
Massage Therapy
203-555-0187
gthrushwell@mailvale.net

```html
<!DOCTYPE html>
<html lang="en">
<head>
<meta charset="utf-8">
<title>Gavin Thrushwell – Licensed Massage Therapist</title>
<link rel="stylesheet" href="https://fonts.googleapis.com/css2?family=Sorts+Mill+Goudy&display=swap">
<style>
  :root {
    --ink: #7a3a1f;
    --foam: #f1ede7;
    --water: #d9cab8;
    --sand-light: #cdb198;
    --sand: #c6a78a;
    --sand-deep: #bf9f82;
    --divider: #8a4a2c;
    --mark-tint: rgba(240, 226, 212, 0.45);
  }
  html, body {
    margin: 0;
    padding: 0;
    width: 1200px;
    height: 900px;
    overflow: hidden;
    background: #ffffff;
  }
  .card {
    position: relative;
    width: 1200px;
    height: 900px;
    overflow: hidden;
    font-family: "Sorts Mill Goudy", Georgia, serif;
    color: var(--ink);
  }
  .beach-backdrop {
    position: absolute;
    inset: 0;
    background: linear-gradient(
      to bottom,
      var(--foam) 0%,
      var(--foam) 12%,
      var(--water) 22%,
      var(--sand-light) 32%,
      var(--sand) 60%,
      var(--sand-deep) 100%
    );
  }
  .athlete-marks {
    position: absolute;
    left: 720px;
    top: 690px;
    width: 480px;
    height: 170px;
    border-radius: 60px;
    background: var(--mark-tint);
  }
  .name,
  .title,
  .phone,
  .email,
  .specialty {
    position: absolute;
    margin: 0;
    line-height: 1;
    font-weight: 400;
    white-space: nowrap;
  }
  .name {
    left: 24px;
    top: 370px;
    font-size: 108px;
  }
  .title {
    left: 24px;
    top: 497px;
    font-size: 64px;
  }
  .phone {
    left: 24px;
    top: 684px;
    font-size: 60px;
  }
  .email {
    left: 24px;
    top: 776px;
    font-size: 60px;
  }
  .divider {
    position: absolute;
    left: 918px;
    top: 290px;
  }
  .specialties {
    position: absolute;
    left: 966px;
    top: 0;
    margin: 0;
    padding: 0;
    list-style: none;
  }
  .specialty {
    left: 0;
    font-size: 42px;
  }
  .specialty:nth-child(1) { top: 330px; }
  .specialty:nth-child(2) { top: 406px; }
  .specialty:nth-child(3) { top: 482px; }
  .specialty:nth-child(4) { top: 558px; }
</style>
</head>
<body>
  <main class="card">
    <div class="beach-backdrop" role="img" aria-label="Photo of a sandy beach with a white wave washing in along the top"></div>
    <div class="athlete-marks" role="img" aria-label="Faint swimmer and cyclist figures drawn in the sand"></div>

    <h1 class="name">Gavin Thrushwell</h1>
    <p class="title">Licensed Massage Therapist</p>

    <p class="phone">203-555-0187</p>
    <p class="email">gthrushwell@mailvale.net</p>

    <svg class="divider" width="12" height="356" viewBox="0 0 12 356" aria-hidden="true">
      <line x1="6" y1="0" x2="6" y2="356" stroke="var(--divider)" stroke-width="6" stroke-dasharray="26 20"/>
    </svg>

    <ul class="specialties">
      <li class="specialty">Swedish</li>
      <li class="specialty">Deep Tissue</li>
      <li class="specialty">Sports</li>
      <li class="specialty">Hot Stone</li>
    </ul>
  </main>
</body>
</html>
```